TRESSLY FACEBOOK DESIGN

I need new design for facebook https://www.facebook.com/tresslyitalia.
Our Businnes is Hair care , hair replacement , hair transplant . hair regrowth . i NEED MEDICAL AND PROFESSIONAL DESIGN. I NEED ALSO RESPONSIVE DESIGN

Target Market(s)

Consumers

Industry/Entity Type

MEDICAL AND COSMETICS

Colors
0054AA
0677BA
7BADD7
CADEEF
E8F1F8

Requirements
Must have
• MEDICAL
Nice to have
• RESPONSIVE DESIGN

```html
<!DOCTYPE html>
<html lang="it">
<head>
<meta charset="utf-8">
<title>Tressly – Facebook Cover</title>
<link rel="stylesheet" href="https://fonts.googleapis.com/css2?family=Montserrat:wght@600&family=Poppins:wght@300;400;600&display=swap">
<style>
  :root {
    --navy: #0054AA;
    --ocean: #0677BA;
    --sky: #33AEE0;
    --sky-soft: #7BADD7;
    --mist: #CADEEF;
    --canvas: #E9EAF5;
    --accent: #4A8AE6;
    --ink: #1C2433;
    --ink-soft: #3A4150;
  }
  * { margin: 0; padding: 0; box-sizing: border-box; }
  html, body { width: 1200px; height: 445px; overflow: hidden; background: var(--canvas); }
  .cover {
    position: relative; width: 1200px; height: 445px; overflow: hidden;
    background: var(--canvas); font-family: "Poppins", sans-serif; color: var(--ink);
  }
  .backdrop { position: absolute; inset: 0; width: 1200px; height: 445px; }

  .brand { position: absolute; left: 105px; top: 16px; display: flex; align-items: center; gap: 6px; }
  .brand-dot { width: 14px; height: 14px; border-radius: 50%; background: var(--ocean); }
  .brand-name { font-family: "Poppins", sans-serif; font-weight: 600; font-size: 19px; color: var(--ocean); letter-spacing: -0.2px; }

  .headline {
    position: absolute; left: 100px; top: 80px;
    font-family: "Montserrat", sans-serif; font-weight: 600; font-size: 29.5px;
    line-height: 40px; letter-spacing: 2.2px; color: var(--accent);
  }
  .headline-rule { position: absolute; left: 100px; top: 170px; width: 28px; height: 3px; background: var(--accent); }

  .services-rail { position: absolute; left: 88px; top: 183px; width: 1.5px; height: 142px; background: var(--accent); }
  .services-title { position: absolute; left: 118px; top: 208px; font-size: 23px; font-weight: 300; color: var(--ink); }
  .services-title strong { font-weight: 600; color: var(--accent); }
  .services-title-rule { position: absolute; left: 118px; top: 241px; width: 13px; height: 4px; background: var(--ink); }

  .service { position: absolute; width: 190px; }
  .service-head { display: flex; align-items: center; gap: 8px; }
  .service-icon { width: 12px; height: 12px; border-radius: 50%; background: var(--accent); display: flex; align-items: center; justify-content: center; }
  .service-name { font-size: 12px; font-weight: 400; color: var(--ink-soft); }
  .service-name strong { font-weight: 600; color: var(--ink); }
  .service-text { margin: 6px 0 0 20px; font-size: 5.2px; line-height: 9.6px; color: var(--ink); text-align: justify; }

  .contact-title { position: absolute; left: 127px; top: 388px; font-size: 15px; font-weight: 400; color: var(--ink); }
  .contact-title strong { font-weight: 600; color: var(--accent); }
  .contact-row { position: absolute; top: 413px; display: flex; align-items: center; gap: 7px; font-size: 7.6px; color: var(--ink-soft); }
  .contact-icon { width: 15px; height: 15px; border-radius: 50%; background: var(--navy); display: flex; align-items: center; justify-content: center; }

  .portrait {
    position: absolute; left: 650px; top: 8px; width: 430px; height: 437px;
    border-radius: 150px 150px 0 0;
    background: linear-gradient(180deg, rgba(238,226,216,0.9) 0%, rgba(244,244,248,0.95) 40%, rgba(226,230,240,0.95) 100%);
  }
</style>
</head>
<body>
<main class="cover">
  <svg class="backdrop" viewBox="0 0 1200 445" aria-hidden="true">
    <path d="M0 0 H20 C55 40 55 160 30 205 C55 240 60 320 35 360 C55 395 50 430 40 445 H0 Z" fill="var(--ocean)"/>
    <path d="M0 0 H15 C50 45 48 150 0 205 Z" fill="var(--navy)"/>
    <path d="M0 225 C40 255 42 330 0 360 Z" fill="var(--sky)" opacity="0.7"/>
    <path d="M745 0 C690 30 650 110 610 170 C580 220 585 300 640 335 L760 445 H1200 V0 Z" fill="var(--navy)"/>
    <path d="M1040 0 H1200 V40 L830 445 H690 L690 420 Z" fill="var(--sky)"/>
    <path d="M1160 0 H1200 V120 L1010 330 L975 330 Z" fill="var(--canvas)"/>
    <path d="M1200 150 V445 H1060 L1200 290 Z" fill="var(--navy)"/>
  </svg>

  <div class="brand">
    <span class="brand-dot"></span>
    <span class="brand-name">Tressly</span>
  </div>

  <h1 class="headline">TRESSLY, CURA E<br>REINTEGRAZIONE DEI CAPELLI</h1>
  <div class="headline-rule"></div>

  <div class="services-rail"></div>
  <h2 class="services-title">WE <strong>PROVIDE YOU</strong></h2>
  <div class="services-title-rule"></div>

  <section class="service" style="left:118px;top:255px;">
    <div class="service-head">
      <span class="service-icon"><svg width="7" height="7" viewBox="0 0 10 10"><circle cx="5" cy="5" r="3" fill="none" stroke="#fff" stroke-width="1.5"/></svg></span>
      <span class="service-name">Hair <strong>Care</strong></span>
    </div>
    <p class="service-text">Gentle scalp treatments and nourishing routines that keep your hair strong, healthy and full of life every day.</p>
  </section>

  <section class="service" style="left:358px;top:255px;">
    <div class="service-head">
      <span class="service-icon"><svg width="7" height="7" viewBox="0 0 10 10"><path d="M2 8 L5 2 L8 8 Z" fill="none" stroke="#fff" stroke-width="1.4"/></svg></span>
      <span class="service-name">Hair <strong>Replacement</strong></span>
    </div>
    <p class="service-text">Natural looking hair systems, custom fitted by our specialists to restore volume, confidence and a fresh look.</p>
  </section>

  <section class="service" style="left:118px;top:309px;">
    <div class="service-head">
      <span class="service-icon"><svg width="7" height="7" viewBox="0 0 10 10"><path d="M5 9 V3 M2.5 5 L5 2 L7.5 5" fill="none" stroke="#fff" stroke-width="1.4"/></svg></span>
      <span class="service-name">Hair <strong>Regrowth</strong></span>
    </div>
    <p class="service-text">Clinically tested therapies that wake up dormant follicles and support steady, visible regrowth over time.</p>
  </section>

  <section class="service" style="left:358px;top:309px;">
    <div class="service-head">
      <span class="service-icon"><svg width="7" height="7" viewBox="0 0 10 10"><rect x="2" y="2.5" width="6" height="5" fill="none" stroke="#fff" stroke-width="1.3"/></svg></span>
      <span class="service-name">Hair <strong>Transplant</strong></span>
    </div>
    <p class="service-text">Modern transplant techniques performed by expert surgeons for permanent, natural results with minimal recovery.</p>
  </section>

  <h2 class="contact-title">CONTACT <strong>US</strong></h2>

  <div class="contact-row" style="left:127px;">
    <span class="contact-icon"><svg width="9" height="9" viewBox="0 0 10 10"><path d="M2 1.5 L3.8 1.5 L4.3 3.6 L3.2 4.4 C3.8 5.6 4.5 6.3 5.7 6.9 L6.5 5.8 L8.5 6.3 L8.5 8.2 C5 8.5 1.6 5 2 1.5 Z" fill="#fff"/></svg></span>
    <span>+39 800 412 638</span>
  </div>
  <div class="contact-row" style="left:230px;">
    <span class="contact-icon"><svg width="9" height="9" viewBox="0 0 10 10" fill="none" stroke="#fff" stroke-width="0.9"><circle cx="5" cy="5" r="3.8"/><ellipse cx="5" cy="5" rx="1.6" ry="3.8"/><path d="M1.2 5 H8.8"/></svg></span>
    <span>https://www.tressly.it/</span>
  </div>
  <div class="contact-row" style="left:339px;">
    <span class="contact-icon"><svg width="9" height="9" viewBox="0 0 10 10" fill="none" stroke="#fff" stroke-width="0.9"><rect x="1.5" y="2.5" width="7" height="5"/><path d="M1.5 2.5 L5 5.5 L8.5 2.5"/></svg></span>
    <span>info@tressly.it</span>
  </div>
  <div class="contact-row" style="left:450px;">
    <span class="contact-icon"><svg width="9" height="9" viewBox="0 0 10 10"><path d="M5 1.5 L9 5 H7.8 V8.5 H5.8 V6.3 H4.2 V8.5 H2.2 V5 H1 Z" fill="#fff"/></svg></span>
    <span>12/2 Street address,City Here</span>
  </div>

  <div class="portrait" role="img" aria-label="Smiling doctor in a white coat with a stethoscope, presenting the services with an open hand"></div>
</main>
</body>
</html>
```